Start up business website

IT Support provider that caters towards law enforcement / police departments. We'll offer remote IT support, backup / recovery services and cyber security. Will add updates soon.

Target Market(s)

Police departments / Law Enforcement

Coding

Coded - Design and coding required

Number of Pages Required

5+ page

Font styles to use
Other font styles liked:
• Use font style in uploaded logo

Colors
0054AA
0677BA
7BADD7
CADEEF
E8F1F8

```html
<!DOCTYPE html>
<html lang="en">
<head>
<meta charset="utf-8">
<title>Bulwark Support Services</title>
<link href="https://fonts.googleapis.com/css2?family=Audiowide&family=Roboto:wght@400;500;700&display=swap" rel="stylesheet">
<style>
:root{
  --blue-deep:#0054AA;
  --blue:#0677BA;
  --blue-mid:#7BADD7;
  --blue-pale:#CADEEF;
  --blue-mist:#E8F1F8;
  --cyan:#29B6EC;
  --navy:#062a5c;
  --night:#061726;
  --ink:#1a1a1a;
  --grey:#777;
  --white:#fff;
  --black:#000;
}
*{margin:0;padding:0;box-sizing:border-box}
html,body{width:1200px;height:3192px;overflow:hidden;background:var(--white)}
body{position:relative;font-family:'Roboto',Arial,sans-serif;color:var(--ink)}
.abs{position:absolute}
.display{font-family:'Audiowide',Arial,sans-serif;text-transform:uppercase}

/* header */
.site-header{position:absolute;left:0;top:0;width:1200px;height:103px;background:var(--white)}
.brand{position:absolute;display:flex;align-items:center;gap:10px}
.brand-mark{border-radius:50%;background:var(--blue-deep);flex:none}
.brand-name{font-family:'Audiowide',Arial,sans-serif;color:var(--blue-deep);line-height:1}
.brand-name span{display:block}
.main-nav{position:absolute;top:43px;left:366px;font-size:11.5px;font-weight:700;color:#222;letter-spacing:.2px}
.main-nav a{position:absolute;white-space:nowrap;color:inherit;text-decoration:none}
.phone{position:absolute;left:852px;top:27px;display:flex;align-items:center;gap:14px}
.phone-icon{width:38px;height:38px;border-radius:50%;background:var(--blue-deep);display:flex;align-items:center;justify-content:center}
.phone-number{font-family:'Audiowide',Arial,sans-serif;color:var(--blue-deep);font-size:24px;white-space:nowrap}

/* hero */
.hero-visual{position:absolute;left:0;top:103px;width:1200px;height:650px;background:radial-gradient(circle at 600px 250px,#1d6f86 0,#0d3f55 22%,#07202f 45%,var(--night) 75%)}
.hero-cut{position:absolute;left:0;top:600px}
.hero-title{position:absolute;left:0;top:248px;width:1200px;text-align:center;color:var(--white);font-size:42px;line-height:52px;letter-spacing:1px;font-weight:400}
.hero-text{position:absolute;left:262px;top:364px;width:676px;text-align:center;color:var(--white);font-size:14px;line-height:28px}
.btn{position:absolute;display:flex;align-items:center;justify-content:center;border-radius:30px;background:var(--blue-deep);color:var(--white);font-family:'Audiowide',Arial,sans-serif;text-transform:uppercase;font-size:14px;letter-spacing:.5px}
.slider-dots{position:absolute;left:568px;top:667px;display:flex;gap:5px}
.slider-dots i{width:12px;height:12px;border-radius:50%;border:1.5px solid var(--white);display:block}
.slider-dots i.on{background:var(--white)}

/* about */
.about-photo{position:absolute;left:155px;top:828px;width:394px;height:458px;background:linear-gradient(135deg,var(--blue-mist) 0,var(--blue-pale) 35%,#2b3a4c 65%,#121a24 100%);clip-path:path('M197 0 C160 30 110 40 60 30 L10 120 C0 260 60 400 197 458 C334 400 394 260 384 120 L334 30 C284 40 234 30 197 0 Z')}
.section-title{font-family:'Audiowide',Arial,sans-serif;text-transform:uppercase;font-weight:400;font-size:38px;line-height:37px;color:var(--blue-deep);white-space:nowrap}
.section-title .accent{color:var(--blue)}
.rule{position:absolute;height:3px;width:57px;background:var(--blue)}
.about-text{position:absolute;left:637px;top:927px;width:428px;font-size:13px;line-height:28px;color:var(--ink)}

/* services */
.services{position:absolute;left:0;top:1380px;width:1200px;height:687px;background:radial-gradient(circle at 622px 300px,#10589e 0,#0a3d7e 35%,var(--navy) 80%)}
.services-title{position:absolute;left:0;top:1452px;width:1200px;text-align:center;color:var(--white);font-size:38px;font-weight:400}
.center-text{position:absolute;text-align:center;font-size:13.3px;line-height:29px}
.card{position:absolute;top:1657px;width:287px;height:323px;background:var(--white);border-radius:6px;text-align:center}
.card.active{background:var(--blue)}
.card h3{position:absolute;left:0;top:70px;width:100%;font-family:'Audiowide',Arial,sans-serif;font-weight:400;font-size:19px;color:var(--blue);text-transform:uppercase;letter-spacing:.3px;white-space:nowrap}
.card .card-rule{position:absolute;left:124px;top:110px;width:40px;height:4px;background:var(--blue-deep)}
.card p{position:absolute;left:16px;top:131px;width:255px;font-size:13px;line-height:28px;color:#444}
.card .more{position:absolute;left:0;top:277px;width:100%;font-family:'Audiowide',Arial,sans-serif;font-size:17px;color:var(--blue);text-transform:uppercase}
.card.active h3,.card.active p,.card.active .more{color:var(--white)}
.card.active .card-rule{background:var(--white)}
.badge{position:absolute;top:1602px;width:102px;height:118px}

/* news */
.news-title{position:absolute;left:0;top:2138px;width:1200px;text-align:center;font-size:37px;color:var(--blue);font-weight:400}
.news-item{position:absolute;left:155px;width:441px;padding:0 17px}
.news-item h4{font-size:14.3px;line-height:28px;font-weight:700;color:var(--ink)}
.news-item p{font-size:11.8px;line-height:28px;color:var(--grey);margin-top:3px}
.news-item.featured{background:var(--blue-deep);border-radius:4px}
.news-item.featured h4,.news-item.featured p{color:var(--white)}
.news-photo{position:absolute;left:604px;top:2274px;width:441px;height:373px;background:linear-gradient(120deg,#0a2a55 0,#114e9a 45%,#0a1d3b 100%)}

/* footer */
.footer-shape{position:absolute;left:0;top:2720px}
.footer-nav{position:absolute;top:2970px;left:0;width:1200px;display:flex;justify-content:center;gap:29px;color:var(--white);font-size:11.5px;font-weight:700}
.socials{position:absolute;top:3013px;left:497px;display:flex;gap:13px}
.social{width:60px;height:60px;border-radius:50%;background:var(--white);border:4px solid #8a8a8a;display:flex;align-items:center;justify-content:center}
.social span{width:16px;height:16px;border-radius:50%;background:var(--blue-deep);display:block}
.copyright{position:absolute;top:3092px;left:0;width:1200px;text-align:center;color:var(--white);font-size:11.5px}
.copyright b{font-family:'Audiowide',Arial,sans-serif;font-weight:400;text-transform:uppercase;font-size:11.5px}
</style>
</head>
<body>

<header class="site-header">
  <div class="brand" style="left:86px;top:18px">
    <span class="brand-mark" style="width:60px;height:60px"></span>
    <span class="brand-name"><span style="font-size:24px">BULWARK</span><span style="font-size:9.5px;margin-top:3px">SUPPORT SERVICES</span></span>
  </div>
  <nav class="main-nav">
    <a style="left:0">HOME</a>
    <a style="left:63px">ABOUT US</a>
    <a style="left:150px">SERVICES</a>
    <a style="left:236px">BLOG</a>
    <a style="left:295px">PARTNERS</a>
    <a style="left:385px">CONTACTS</a>
  </nav>
  <div class="phone">
    <span class="phone-icon"><svg width="16" height="16" viewBox="0 0 24 24"><path fill="#fff" d="M6.6 10.8a15.1 15.1 0 0 0 6.6 6.6l2.2-2.2c.3-.3.7-.4 1-.2 1.1.4 2.3.6 3.6.6.6 0 1 .4 1 1V20c0 .6-.4 1-1 1A17 17 0 0 1 3 4c0-.6.4-1 1-1h3.5c.6 0 1 .4 1 1 0 1.3.2 2.5.6 3.6.1.3 0 .7-.2 1z"/></svg></span>
    <span class="phone-number">+ 100 555 0199</span>
  </div>
</header>

<section class="hero">
  <div class="hero-visual" role="img" aria-label="Glowing digital globe surrounded by connected network icons on a dark background"></div>
  <svg class="hero-cut" width="1200" height="160" viewBox="0 0 1200 160">
    <polygon points="0,32 597,144 1200,32 1200,160 0,160" fill="#fff"/>
    <polyline points="0,36 597,146 1200,36" fill="none" stroke="#0054AA" stroke-width="9"/>
  </svg>
  <h1 class="hero-title display">We are a<br>managed service provider</h1>
  <p class="hero-text">Lorem ipsum dolor sit amet, consectetur adipiscing elit, sed do eiusmod tempor incididunt ut labore et dolore magna aliqua Ut enim ad minim veniam quis nostrud exercitation ullamco.magna aliqua Ut enim ad minim veniam quis nostrud exercitation ullamco.</p>
  <a class="btn" style="left:508px;top:482px;width:184px;height:49px">Get started</a>
  <div class="slider-dots"><i></i><i class="on"></i><i></i><i></i></div>
</section>

<section class="about">
  <div class="about-photo" role="img" aria-label="Hand in a business suit holding a glowing padlock shield inside a network"></div>
  <h2 class="section-title abs" style="left:637px;top:826px">About <span class="accent">Bulwark</span><br>support services</h2>
  <div class="rule" style="left:637px;top:915px"></div>
  <p class="about-text">Lorem ipsum dolor sit amet, consectetur adipiscing elit, sed do eiusmod tempor incididunt ut labore et dolore magna aliqua. Ut enim ad minim veniam, quis nostrud exercitation ullamco laboris nisi ut aliquip ex ea commodo consequat. Duis aute irure dolor in reprehenderit in voluptate velit esse cillum dolore eu fugiat nulla pariatur. Excepteur sint occaecat cupidatat non proident, sunt in culpa qui officia deserunt mollit anim id est laborum.Sed ut perspiciatis unde omnis iste natus error sit vluptatem accusantium doloremque laudantium, totam rem aperiam, eaque ipsa quae ab illo inventore veritatis et quasi architecto beatae vitae dicta sunt explicabo Nemo enim ipsam voluptatem quia voluptas.</p>
  <a class="btn" style="left:637px;top:1239px;width:185px;height:49px">Learn more</a>
</section>

<section class="services-wrap">
  <div class="services" role="img" aria-label="Deep blue radar dial background"></div>
  <h2 class="services-title display">Our offer services</h2>
  <div class="rule" style="left:572px;top:1505px;background:#fff"></div>
  <p class="center-text" style="left:222px;top:1523px;width:756px;color:#fff">Lorem ipsum dolor sit amet, consectetur adipiscing elit, sed do eiusmod tempor incididunt ut labore et dolore magna aliqua. Ut enim ad minim veniam, quis nostrud exercitation ullamco laboris nisi ut aliquip ex ea commodo consequat.</p>

  <article class="card" style="left:168px">
    <h3>IT Support</h3><div class="card-rule"></div>
    <p>Sed ut perspiciatis unde omnis iste natus error sit voluptatem accusantium dolorem-que laudantium, totam rem aperiam, eaque ipsa quae ab illo inventore veritatis et quasi architecto beatae vitae.</p>
    <span class="more">Learn more</span>
  </article>
  <article class="card active" style="left:475px">
    <h3>Backup / Recovery</h3><div class="card-rule"></div>
    <p>Sed ut perspiciatis unde omnis iste natus error sit voluptatem accusantium dolorem-que laudantium, totam rem aperiam, eaque ipsa quae ab illo inventore veritatis et quasi architecto beatae vitae.</p>
    <span class="more">Learn more</span>
  </article>
  <article class="card" style="left:780px">
    <h3>Cyber Security</h3><div class="card-rule"></div>
    <p>Sed ut perspiciatis unde omnis iste natus error sit voluptatem accusantium dolorem-que laudantium, totam rem aperiam, eaque ipsa quae ab illo inventore veritatis et quasi architecto beatae vitae.</p>
    <span class="more">Learn more</span>
  </article>

  <svg class="badge" style="left:260px" viewBox="0 0 102 118"><path d="M51 2 C40 12 25 14 12 10 L4 28 C0 70 20 100 51 116 C82 100 102 70 98 28 L90 10 C77 14 62 12 51 2Z" fill="#29B6EC"/><circle cx="51" cy="54" r="22" fill="none" stroke="#fff" stroke-width="3"/></svg>
  <svg class="badge" style="left:567px" viewBox="0 0 102 118"><path d="M51 2 C40 12 25 14 12 10 L4 28 C0 70 20 100 51 116 C82 100 102 70 98 28 L90 10 C77 14 62 12 51 2Z" fill="#29B6EC"/><circle cx="51" cy="54" r="22" fill="none" stroke="#fff" stroke-width="3"/></svg>
  <svg class="badge" style="left:873px" viewBox="0 0 102 118"><path d="M51 2 C40 12 25 14 12 10 L4 28 C0 70 20 100 51 116 C82 100 102 70 98 28 L90 10 C77 14 62 12 51 2Z" fill="#29B6EC"/><circle cx="51" cy="54" r="22" fill="none" stroke="#fff" stroke-width="3"/></svg>
</section>

<section class="news">
  <h2 class="news-title display">Our latest news</h2>
  <div class="rule" style="left:572px;top:2191px"></div>
  <p class="center-text" style="left:258px;top:2200px;width:684px;color:#222">Lorem ipsum dolor sit amet, consectetur adipiscing elit, sed do eiusmod tempor incididunt ut labore et dolore magna aliqua. Ut enim ad minim veniam, quis nostrud exercitation ullamco laboris.</p>

  <article class="news-item" style="top:2287px">
    <h4>Lorem ipsum dolor sit amet, consectetur adipiscing elit, sed do eiusmod tempor incidid.</h4>
    <p>Lorem ipsum dolor sit amet, consectetur adipiscing elit, sed do eiusmod tempor incididunt ut labore et dolore magna aliqua. Quis ipsum sus-pendisse ultrices gravida. Risus commodo viverra.</p>
  </article>
  <article class="news-item featured" style="top:2468px;height:179px;padding-top:13px">
    <h4>Lorem ipsum dolor sit amet, consectetur adipiscing elit, sed do eiusmod tempor incidid.</h4>
    <p>Lorem ipsum dolor sit amet, consectetur adipiscing elit, sed do eiusmod tempor incididunt ut labore et dolore magna aliqua. Quis ipsum sus-pendisse ultrices gravida. Risus commodo viverra.</p>
  </article>
  <div class="news-photo" role="img" aria-label="IT technician working at multiple monitors in a blue-lit operations room"></div>
</section>

<footer>
  <svg class="footer-shape" width="1200" height="472" viewBox="0 0 1200 472">
    <polygon points="0,124 602,16 1200,124 1200,472 0,472" fill="#000"/>
    <polyline points="0,114 602,5 1200,114" fill="none" stroke="#0677BA" stroke-width="9"/>
  </svg>
  <div class="brand" style="left:438px;top:2830px;gap:14px">
    <span class="brand-mark" style="width:100px;height:100px;background:#fff"></span>
    <span class="brand-name" style="color:#fff"><span style="font-size:36px">BULWARK</span><span style="font-size:13px;margin-top:4px">SUPPORT SERVICES</span></span>
  </div>
  <nav class="footer-nav"><span>HOME</span><span>ABOUT US</span><span>SERVICES</span><span>BLOG</span><span>PARTNERS</span><span>CONTACTS</span></nav>
  <div class="socials">
    <a class="social" aria-label="Social profile"><span></span></a>
    <a class="social" aria-label="Social profile"><span></span></a>
    <a class="social" aria-label="Social profile"><span></span></a>
  </div>
  <p class="copyright">© Copyright 2021 &nbsp;<b>Bulwark Support Services</b> &nbsp; | &nbsp; All Rights Reserved</p>
</footer>

</body>
</html>
```